business card for horse saddlery

after a new business card for our saddlery, i will add 2 logos we have previously used and they can be used (or not) . Any images can be used from our website also at www.bramwoods.net.au, I have also added our brand logo, which may be good to incorporate on back ? we have over 15, 000 items online, ship Australia Wide.

Target Market(s)

horse owners

Industry/Entity Type

Retail - Equestrian

Contact Information for Business Card

Bramwood Horse Supplies, 1300 62 48 07, www.bramwoods.net.au, 278 Tallowmere Rd Corrindale Q 4602

Requirements
Must have
• ridelark is our brand so ridelark logo on back as 'distributers of', easy to read
Nice to have
• professional but fun
Should not have
• double sided (description wont save double sided)

```html
<!DOCTYPE html>
<html lang="en">
<head>
<meta charset="utf-8">
<title>Bramwood Horse Supplies – Business Card</title>
<link rel="stylesheet" href="https://fonts.googleapis.com/css2?family=Open+Sans:wght@400;600;700&display=swap">
<style>
  :root {
    --backdrop: #232323;
    --card: #ffffff;
    --navy: #2b3f86;
    --amber: #fbb01b;
    --ink: #1c1c1c;
    --wave-light: #eeeeef;
    --wave-mid: #d9d9db;
    --icon-blue: #3d6fc4;
  }
  * { box-sizing: border-box; margin: 0; padding: 0; }
  html, body { width: 1200px; height: 780px; overflow: hidden; }
  body {
    background: var(--backdrop);
    font-family: "Open Sans", Arial, sans-serif;
    position: relative;
  }
  .card {
    position: absolute;
    top: 70px;
    width: 380px;
    height: 640px;
    background: var(--card);
    border-radius: 28px;
    overflow: hidden;
  }
  .card--front { left: 170px; }
  .card--back { left: 650px; }

  /* Front */
  .front-brand {
    position: absolute;
    top: 50%;
    left: 50%;
    transform: translate(-50%, -50%) rotate(-90deg);
    display: flex;
    align-items: center;
    gap: 18px;
    white-space: nowrap;
  }
  .front-brand__dot {
    width: 120px; height: 120px;
    border-radius: 50%;
    background: var(--amber);
    flex: none;
  }
  .front-brand__name {
    font-weight: 600;
    font-size: 34px;
    line-height: 1.1;
    color: var(--navy);
  }

  /* Back */
  .back-brand {
    position: absolute;
    top: 42px; left: 0; right: 0;
    display: flex;
    justify-content: center;
    align-items: center;
    gap: 10px;
  }
  .back-brand__dot {
    width: 34px; height: 34px;
    border-radius: 50%;
    background: var(--amber);
  }
  .back-brand__name {
    font-weight: 600;
    font-size: 17px;
    color: var(--navy);
    line-height: 1.15;
  }
  .portrait {
    position: absolute;
    top: 128px;
    left: 50%;
    transform: translateX(-50%);
    width: 128px; height: 128px;
    border-radius: 50%;
    border: 3px solid var(--amber);
    background: radial-gradient(circle at 45% 40%, #d9dadc 0%, #8a8c90 35%, #0d0d0d 70%);
  }
  .contact {
    position: absolute;
    top: 272px; left: 0; right: 0;
    text-align: center;
    color: var(--ink);
  }
  .contact__name {
    font-weight: 700;
    font-size: 28px;
    color: var(--amber);
    line-height: 1.1;
  }
  .contact__role {
    font-size: 15px;
    font-weight: 600;
    margin-top: 2px;
  }
  .contact__icons {
    display: flex;
    justify-content: center;
    gap: 14px;
    margin: 10px 0 6px;
  }
  .icon {
    width: 20px; height: 20px;
    border-radius: 50%;
    background: var(--icon-blue);
    border: 2px solid var(--amber);
    display: flex; align-items: center; justify-content: center;
  }
  .icon svg { width: 11px; height: 11px; }
  .contact__phone { font-size: 21px; font-weight: 600; }
  .contact__web { font-size: 14px; font-weight: 600; }
  .contact__icons--single { margin-top: 14px; }
  .contact__address { font-size: 14px; font-weight: 600; line-height: 1.35; }

  .waves {
    position: absolute;
    left: 0; bottom: 0;
    width: 380px; height: 250px;
  }
  .partners {
    position: absolute;
    bottom: 40px; left: 150px; right: 20px;
    display: flex;
    justify-content: space-around;
    align-items: center;
  }
  .partner {
    display: flex; align-items: center; gap: 6px;
    font-size: 14px; font-weight: 600;
    color: var(--navy);
  }
  .partner__mark {
    width: 14px; height: 14px;
    border-radius: 50%;
    background: var(--navy);
  }
</style>
</head>
<body>

  <section class="card card--front">
    <div class="front-brand">
      <span class="front-brand__dot"></span>
      <span class="front-brand__name">Bramwood<br>Horse Supplies</span>
    </div>
  </section>

  <section class="card card--back">
    <div class="back-brand">
      <span class="back-brand__dot"></span>
      <span class="back-brand__name">Bramwood<br>Horse Supplies</span>
    </div>

    <div class="portrait" role="img" aria-label="Photo of a grey horse wearing a bridle against a black background"></div>

    <div class="contact">
      <p class="contact__name">Marta Lindqvist</p>
      <p class="contact__role">Horse owners</p>
      <div class="contact__icons">
        <span class="icon"><svg viewBox="0 0 12 12"><path d="M3 1l2 2.4-1.2 1.2a6 6 0 0 0 3.6 3.6L8.6 7 11 9l-1.4 1.8C5.6 10.6 1.4 6.4 1.2 2.4z" fill="#fff"/></svg></span>
        <span class="icon"><svg viewBox="0 0 12 12" fill="none" stroke="#fff" stroke-width="1.2"><circle cx="6" cy="6" r="4.8"/><ellipse cx="6" cy="6" rx="2" ry="4.8"/><path d="M1.2 6h9.6"/></svg></span>
      </div>
      <p class="contact__phone">1300 62 48 07</p>
      <p class="contact__web">www.bramwoods.net.au</p>
      <div class="contact__icons contact__icons--single">
        <span class="icon"><svg viewBox="0 0 12 12"><path d="M6 11S2.2 6.8 2.2 4.6a3.8 3.8 0 0 1 7.6 0C9.8 6.8 6 11 6 11z" fill="#fff"/><circle cx="6" cy="4.6" r="1.4" fill="#3d6fc4"/></svg></span>
      </div>
      <p class="contact__address">278 Tallowmere Rd<br>Corrindale Q 4602</p>
    </div>

    <svg class="waves" viewBox="0 0 380 250" preserveAspectRatio="none" aria-hidden="true">
      <defs>
        <linearGradient id="waveShade" x1="0" y1="0" x2="0" y2="1">
          <stop offset="0" stop-color="#c9c9cc"/>
          <stop offset="1" stop-color="#ffffff"/>
        </linearGradient>
      </defs>
      <path d="M0 110 C120 150 300 130 380 0 L380 250 L0 250 Z" fill="url(#waveShade)"/>
      <path d="M0 125 C130 160 300 150 380 60 L380 250 L0 250 Z" fill="var(--wave-light)"/>
      <path d="M60 250 C120 170 200 140 260 135 C310 130 350 110 380 90 L380 250 Z" fill="url(#waveShade)" opacity="0.6"/>
      <path d="M100 250 C150 190 220 160 380 140 L380 250 Z" fill="#ffffff"/>
    </svg>

    <div class="partners">
      <span class="partner"><span class="partner__mark"></span>Bramwood</span>
      <span class="partner">ridelark</span>
    </div>
  </section>

</body>
</html>
```